Healthy Sweets Manufacturer Needs Series of Card

We need a catchy series of cards (business card size) for display with our super healthy range of sweets in cafe cake cabinets. We are thinking maybe a groovy bean cartoon in different poses (since our cakes are made from white kidney beans) eg. Bean holding dumbells promoting High Protein, Skinny Bean promoting Low Calorie etc etc. Other cards to illustrate: Coconut oil, Low calorie, Low sugar, All natural, Superfood Ingredients, 'Made from Beans', Diabetic Friendly, Low GI, High Protein, Super Healthy, Dairy Free. Also 1 generic card that displays the name of product for sale. We have approx. 12 product lines for sale. Our logo is attached. Our target market is broad - anyone who loves cake. We really want to push the healthy aspects of our product and keep it fun and inviting.
Business Card Size. We would like you to create a fun bean character that presents in different poses on each card.
eg.
Card 1 - Bean character holding dumbells looking strong.
Card 2 - Bean character with sweatband like its been working out.
Card 3 - 'Skinny' Bean character like its slimmed right down
Card 4 - Bean character doing a one handed pushup.
Card 5 - Svelte looking bean character with lovely lashes and lipstick etc
Card 6 - A bean character with bulging muscles
Card 7 - An organic bean character
Card 8 - An athletic bean character.
Card 9 - An active bean character
Card 10 - A bean character with bikinis looking good.
Overall, these characters are to appear 'active' and 'healthy' as this is the message we are trying to get across.
All of these cards will be overlayed with health messages about our products such as "High Protein - Low Carbs", "Low to No Sugar", "Coconut Oil - The Good Fat", "The Healthy Treat" etc etc.
Updates
Project Deadline Extended
Reason: To All the designers that I have contacted, please submit the rest of your drawings. Thankyou.
Target Market(s)
Anyone who loves cake.
Industry/Entity Type
Business
Look and feel
Each slider illustrates characteristics of the customer's brand and the style your logo design should communicate.

```html
<!DOCTYPE html>
<html lang="en">
<head>
<meta charset="utf-8">
<title>Pip Bakes – Low to No Sugar cards</title>
<link href="https://fonts.googleapis.com/css2?family=Questrial&display=swap" rel="stylesheet">
<style>
  :root {
    --page-bg: #f1ece4;
    --card-white: #ffffff;
    --lime: #b3d13a;
    --lime-text: #a6c631;
    --sun: #f9bc2a;
    --sun-text: #f4b21f;
    --bean-cream: #f3efd2;
    --bean-shadow: rgba(70, 60, 40, 0.35);
    --card-shadow: rgba(60, 45, 25, 0.18);
  }
  * { box-sizing: border-box; margin: 0; padding: 0; }
  html, body {
    width: 1200px;
    height: 678px;
    overflow: hidden;
    background: var(--page-bg);
    font-family: "Questrial", "Century Gothic", sans-serif;
  }
  .card-set {
    position: relative;
    width: 1200px;
    height: 678px;
    display: flex;
    align-items: center;
    justify-content: center;
    gap: 60px;
  }
  .card {
    width: 530px;
    height: 303px;
    display: flex;
    background: var(--card-white);
    box-shadow: 0 6px 18px var(--card-shadow);
  }
  .card__message-side {
    flex: 0 0 52%;
    padding: 30px 28px 32px;
    display: flex;
    flex-direction: column;
    justify-content: space-between;
  }
  .brand {
    display: flex;
    align-items: center;
    gap: 8px;
    font-size: 24px;
    letter-spacing: 0.5px;
  }
  .brand__dot {
    width: 14px;
    height: 14px;
    border-radius: 50%;
    background: currentColor;
  }
  .health-message {
    font-size: 46px;
    line-height: 1.08;
    text-transform: uppercase;
    font-weight: 400;
    letter-spacing: 0.5px;
  }
  .card__character {
    flex: 1;
    position: relative;
  }
  /* soft placeholder for the bean character: cream body glow over a ground shadow */
  .card__character::before {
    content: "";
    position: absolute;
    left: 50%;
    top: 46%;
    width: 150px;
    height: 190px;
    transform: translate(-50%, -50%);
    border-radius: 50%;
    background: radial-gradient(ellipse at center, var(--bean-cream) 0%, var(--bean-cream) 35%, rgba(243, 239, 210, 0) 72%);
  }
  .card__character::after {
    content: "";
    position: absolute;
    left: 50%;
    bottom: 34px;
    width: 130px;
    height: 26px;
    transform: translateX(-50%);
    border-radius: 50%;
    background: radial-gradient(ellipse at center, var(--bean-shadow) 0%, rgba(70, 60, 40, 0) 72%);
  }
  .card--lime .brand,
  .card--lime .health-message { color: var(--lime-text); }
  .card--lime .card__character { background: var(--lime); }
  .card--sun .brand,
  .card--sun .health-message { color: var(--sun-text); }
  .card--sun .card__character { background: var(--sun); }
</style>
</head>
<body>
  <main class="card-set">
    <article class="card card--lime">
      <div class="card__message-side">
        <div class="brand"><span class="brand__dot"></span>Pip Bakes</div>
        <h2 class="health-message">Low<br>to no<br>sugar</h2>
      </div>
      <div class="card__character" role="img" aria-label="Illustration area: cartoon bean character in yellow shorts lifting a dumbbell, sweating"></div>
    </article>

    <article class="card card--sun">
      <div class="card__message-side">
        <div class="brand"><span class="brand__dot"></span>Pip Bakes</div>
        <h2 class="health-message">Low<br>to no<br>sugar</h2>
      </div>
      <div class="card__character" role="img" aria-label="Illustration area: cartoon bean character in green shorts doing a one-handed push-up"></div>
    </article>
  </main>
</body>
</html>
```